Website for our 3rd party logistics warehouse company

Our company is a 3rd party logistics company. We receive and ship other businesses products for them. We offer our services to other smaller businesses that do not have a warehouse to operate out of. We also help many Brindlemart businesses prepare their products to be sold on Brindlemart.

We are looking for a modern looking design for our website. Please see our attached logo for design ideas. We are open to changing logo colors for website.

We really like the look of the website www.quorvela.com

Target Market(s)

Other businesses and brands of products

Industry/Entity Type

Warehousing and shipping

Number of Pages Required

2 page

Requirements
Must have
• We need 2 pages. Our main landing page and a duplicate page with different information geared towards brands.
Nice to have
• I like the look of overlay/transparent sections. Please see quorvela.com there is a ribbon that shows "Partners".

```html
<!DOCTYPE html>
<html lang="en">
<head>
<meta charset="utf-8">
<title>Halvorn 3PL – Warehousing &amp; Fulfilment</title>
<link rel="stylesheet" href="https://fonts.googleapis.com/css2?family=Krona+One&family=Roboto:wght@400;500;700&display=swap">
<style>
:root{
  --yellow:#fbc63c;
  --yellow-deep:#f5b71f;
  --ink:#141414;
  --text:#333;
  --muted:#555;
  --rule:#d8d8d8;
  --soft:#f4f4f4;
  --white:#fff;
  --head:"Krona One",sans-serif;
  --body:"Roboto",sans-serif;
}
*{box-sizing:border-box;margin:0;padding:0}
html,body{width:1200px;height:4087px;overflow:hidden}
body{position:relative;font-family:var(--body);color:var(--text);background:var(--white)}
.abs{position:absolute}
.head{font-family:var(--head);color:var(--ink);text-transform:uppercase;letter-spacing:2px;font-weight:400}
.accent{color:var(--yellow)}
.btn{position:absolute;display:flex;align-items:center;justify-content:center;font:700 15px var(--body);text-transform:uppercase;border-radius:30px;color:var(--ink)}
.btn-solid{background:var(--yellow)}
.btn-line{border:2px solid var(--ink)}

/* hero */
.hero{position:absolute;left:0;top:0;width:1200px;height:632px;overflow:hidden}
.hero-photo{position:absolute;inset:0;background:linear-gradient(160deg,#4b5a3c 0%,#6c6a4a 35%,#8e8565 55%,#5a5440 75%,#2f2b22 100%)}
.hero-shade{position:absolute;inset:0;background:linear-gradient(90deg,rgba(0,0,0,.45),rgba(0,0,0,.05) 60%)}
.logo{position:absolute;font:700 22px var(--body);color:var(--white);letter-spacing:3px;display:flex;align-items:center;gap:10px}
.logo .dot{width:14px;height:14px;border-radius:50%;background:var(--yellow)}
.nav{position:absolute;left:415px;top:38px;display:flex;gap:38px;font:500 15px var(--body);color:var(--white);text-transform:uppercase}
.call{position:absolute;left:935px;top:27px;display:flex;align-items:center;gap:12px;color:var(--white)}
.call .ring{width:40px;height:40px;border-radius:50%;background:var(--yellow);display:flex;align-items:center;justify-content:center}
.call small{display:block;font:500 11px var(--body);text-transform:uppercase}
.call b{font:500 16px var(--body)}
.hero-title{position:absolute;left:127px;top:200px;font:400 38px/52px var(--head);font-style:italic;color:var(--white);letter-spacing:3px;text-transform:uppercase}
.partners{position:absolute;left:0;top:527px;width:1200px;height:105px;background:rgba(20,20,20,.55)}
.partners .label{position:absolute;left:100px;top:10px;font:400 16px var(--body);color:var(--yellow);text-decoration:underline}
.partners .name{position:absolute;top:48px;font:700 26px var(--body);color:var(--white);display:flex;align-items:center;gap:10px}
.partners .sq{width:30px;height:30px;background:var(--white);border-radius:6px}

/* who */
.who{position:absolute;left:100px;top:717px;width:1000px;height:451px;background:var(--white);box-shadow:0 4px 22px rgba(0,0,0,.09);border-radius:4px;overflow:hidden}
.who-text{position:absolute;left:560px;top:90px;width:385px}
.who-text h2{font-size:32px;margin-bottom:34px}
.who-text p{font:400 14.5px/29px var(--body);color:var(--muted)}

/* why */
.section-rule{position:absolute;height:1px;background:var(--rule)}
.why-title{position:absolute;left:0;width:1200px;top:1255px;text-align:center;font-size:31px}
.feature{position:absolute;width:220px;text-align:center;font:500 16px/26px var(--body);color:var(--ink)}
.ring-icon{position:absolute;width:120px;height:120px;border:2px solid var(--yellow);border-radius:50%}

/* guarantee */
.guarantee{position:absolute;left:0;top:1724px;width:1200px;height:549px}
.g-text{position:absolute;left:190px;top:128px;width:340px}
.g-text h2{font-size:31px;line-height:38px;margin-bottom:26px}
.g-text p{font:400 13.5px/27px var(--body);color:var(--ink)}

/* benefits */
.benefits-title{position:absolute;left:0;width:1200px;top:2362px;text-align:center;font-size:33px}
.benefit{position:absolute;width:170px;text-align:center;font:500 14px/22px var(--body);color:var(--ink)}
.vrule{position:absolute;width:1px;top:2440px;height:190px;background:var(--rule)}

/* software */
.software{position:absolute;left:0;top:2711px;width:1200px;height:492px;background:var(--soft)}
.sw-text{position:absolute;left:660px;top:152px;width:450px}
.sw-text h2{font-size:29px;margin-bottom:22px}
.sw-text p{font:400 16px/31px var(--body);color:var(--muted)}

/* contact */
.contact{position:absolute;left:0;top:3203px;width:1200px;height:513px;overflow:hidden}
.contact-yellow{position:absolute;left:0;top:0;width:692px;height:513px;background:var(--yellow)}
.contact-photo{position:absolute;left:692px;top:0;width:508px;height:513px;background:linear-gradient(180deg,#8a7f86 0%,#c7a58e 45%,#e8b77a 70%,#6f5d55 100%)}
.contact h2{position:absolute;left:100px;top:84px;font-size:31px}
.contact .sub{position:absolute;left:100px;top:138px;font:500 22px var(--body);color:var(--ink);text-transform:uppercase;display:flex;align-items:center;gap:18px}
.contact .sub i{display:block;width:34px;height:2px;background:var(--ink)}
.field{position:absolute;background:var(--white);font:400 13px var(--body);color:#444;padding:11px 12px}

/* footer */
.footer{position:absolute;left:0;top:3716px;width:1200px;height:371px;background:#0d0d0d;color:var(--white)}
.footer h4{position:absolute;font:700 18px var(--body);text-transform:uppercase}
.footer ul{position:absolute;list-style:none;font:400 14px/28.5px var(--body)}
.c-item{position:absolute;font:400 14px/21px var(--body);padding-left:26px}
.c-item svg{position:absolute;left:0;top:3px}
.news-input{position:absolute;left:806px;top:135px;width:300px;height:50px;background:var(--white);border-radius:25px;overflow:hidden;font:400 14px var(--body);color:#333;padding:16px 22px}
.news-input .send{position:absolute;right:0;top:0;width:50px;height:50px;background:var(--yellow);display:flex;align-items:center;justify-content:center}
.social{position:absolute;top:228px;width:38px;height:38px;border:1.5px solid var(--white);border-radius:50%}
.copyright{position:absolute;left:0;top:335px;width:1200px;text-align:center;font:400 14px var(--body)}
</style>
</head>
<body>

<!-- HERO -->
<section class="hero">
  <div class="hero-photo" role="img" aria-label="Branded semi truck driving on a mountain highway through pine forest"></div>
  <div class="hero-shade"></div>
  <div class="logo" style="left:100px;top:42px"><span class="dot"></span>HALVORN 3PL</div>
  <nav class="nav"><span>Home</span><span>About Us</span><span>Services</span><span>Software</span><span>Contact</span></nav>
  <div class="call">
    <span class="ring"><svg width="18" height="18" viewBox="0 0 24 24"><path d="M6.6 10.8a15 15 0 0 0 6.6 6.6l2.2-2.2c.3-.3.7-.4 1-.2 1.1.4 2.3.6 3.6.6.6 0 1 .4 1 1V20c0 .6-.4 1-1 1A17 17 0 0 1 3 4c0-.6.4-1 1-1h3.5c.6 0 1 .4 1 1 0 1.3.2 2.5.6 3.6.1.3 0 .7-.2 1z" fill="#fff"/></svg></span>
    <span><small>Give us a call</small><b>+(888) 555-0142</b></span>
  </div>
  <svg class="abs" style="left:60px;top:300px" width="24" height="40"><path d="M20 2 4 20l16 18" fill="none" stroke="#fff" stroke-width="2"/></svg>
  <svg class="abs" style="left:1108px;top:300px" width="24" height="40"><path d="M4 2l16 18L4 38" fill="none" stroke="#fff" stroke-width="2"/></svg>
  <h1 class="hero-title">Grow your<br>business with<br>Halvorn 3PL</h1>
  <span class="btn btn-solid" style="left:127px;top:377px;width:189px;height:50px">Get Started</span>
  <div class="partners">
    <span class="label">Partners</span>
    <span class="name" style="left:100px"><span class="sq"></span>Placeholder</span>
    <span class="name" style="left:405px;font-size:20px">Loomwise</span>
    <span class="name" style="left:643px">Mailcrest</span>
    <span class="name" style="left:882px">PLACEHOLDER</span>
  </div>
</section>

<!-- WHO WE ARE -->
<section class="who">
  <svg class="abs" style="left:0;top:0" width="540" height="451" viewBox="0 0 540 451">
    <defs><linearGradient id="driverTone" x1="0" y1="0" x2="1" y2="1"><stop offset="0" stop-color="#9fb4c4"/><stop offset=".5" stop-color="#5f6f86"/><stop offset="1" stop-color="#3c4a63"/></linearGradient></defs>
    <path d="M0 0H430Q560 225 430 451H0Z" fill="url(#driverTone)" role="img" aria-label="Smiling truck driver seated in his cab"/>
    <path d="M430 0Q560 225 430 451" fill="none" stroke="var(--yellow)" stroke-width="3"/>
  </svg>
  <div class="who-text">
    <h2 class="head">Who we <span class="accent">are</span></h2>
    <p>Halvorn 3PL is your one stop 3PL that will help you grow your business and allow you to be hands off. We offer high end services and meet our commitment, guaranteed.</p>
  </div>
  <span class="btn btn-solid" style="left:560px;top:300px;width:189px;height:48px">Learn More</span>
</section>

<!-- WHY -->
<div class="section-rule" style="left:100px;top:1276px;width:187px"></div>
<div class="section-rule" style="left:913px;top:1276px;width:187px"></div>
<h2 class="why-title head">Why use a <span class="accent">prep 3PL?</span></h2>

<div class="ring-icon" style="left:153px;top:1341px"></div>
<svg class="abs" style="left:183px;top:1371px" width="60" height="60" viewBox="0 0 60 60" fill="none" stroke="var(--yellow)" stroke-width="2"><circle cx="30" cy="30" r="26"/><path d="M12 18c8 2 8 10 14 12s2 14 8 18M38 6c-2 8 6 10 12 8M40 30c4 0 8 4 10 8"/></svg>
<div class="feature" style="left:103px;top:1480px">Work from anywhere in the world.</div>

<div class="ring-icon" style="left:411px;top:1341px"></div>
<svg class="abs" style="left:441px;top:1371px" width="60" height="60" viewBox="0 0 60 60" fill="none" stroke="var(--yellow)" stroke-width="2"><circle cx="20" cy="14" r="6"/><circle cx="40" cy="14" r="6"/><path d="M8 32c2-8 22-8 24 0M28 32c2-8 22-8 24 0M8 42l10-6 12 8 12-8 10 6M18 50l12-6 12 6"/></svg>
<div class="feature" style="left:361px;top:1480px">Don't have to manage employees, health insurance plans, payroll, sick calls, etc.</div>

<div class="ring-icon" style="left:670px;top:1341px"></div>
<svg class="abs" style="left:700px;top:1371px" width="60" height="60" viewBox="0 0 60 60" fill="none" stroke="var(--yellow)" stroke-width="2"><path d="M30 4l6 5 8-1 2 8 7 4-3 7 3 7-7 4-2 8-8-1-6 5-6-5-8 1-2-8-7-4 3-7-3-7 7-4 2-8 8 1z"/><path d="M21 29l6 6 12-12"/><path d="M18 46l-6 12 8-3 4 6 4-10M42 46l6 12-8-3-4 6-4-10"/></svg>
<div class="feature" style="left:620px;top:1480px">Don't get locked into a 3-5 year warehouse lease where you guarantee hundreds of thousands of dollars</div>

<div class="ring-icon" style="left:929px;top:1341px"></div>
<svg class="abs" style="left:959px;top:1371px" width="60" height="60" viewBox="0 0 60 60" fill="none" stroke="var(--yellow)" stroke-width="2"><path d="M6 54h48M10 54V40h8v14M24 54V32h8v22M38 54V24h8v30M8 34l14-10 10 6 20-20M44 10h8v8"/></svg>
<div class="feature" style="left:879px;top:1480px">Grow your business without commitment</div>

<div class="section-rule" style="left:100px;top:1630px;width:1000px"></div>

<!-- GUARANTEE -->
<section class="guarantee">
  <svg class="abs" style="left:0;top:0" width="1200" height="549" viewBox="0 0 1200 549">
    <defs><linearGradient id="warehouseTone" x1="0" y1="0" x2="1" y2="1"><stop offset="0" stop-color="#c9a56a"/><stop offset=".5" stop-color="#6a7a8e"/><stop offset="1" stop-color="#3f4d63"/></linearGradient></defs>
    <path d="M0 0H1100Q1200 0 1200 100V549H0Z" fill="url(#warehouseTone)" role="img" aria-label="Two warehouse workers in safety vests checking boxes between shelving racks"/>
    <polygon points="0,0 733,0 455,549 0,549" fill="var(--yellow)" opacity=".93"/>
    <polygon points="180,0 733,0 600,262" fill="var(--yellow-deep)" opacity=".35"/>
  </svg>
  <div class="g-text">
    <h2 class="head">Our<br>guarantee</h2>
    <p>All orders will be prepped and ready for shipment in 48 business hours (often 24 or less) and we guarantee it. We are confident in our services and if we do not fulfill our obligation, we offer a 500 item (up to $700) credit on your next shipment.</p>
  </div>
  <span class="btn btn-line" style="left:190px;top:373px;width:189px;height:50px">Contact Us</span>
</section>

<!-- BENEFITS -->
<h2 class="benefits-title head">Our <span class="accent">benefits</span></h2>

<svg class="abs" style="left:132px;top:2441px" width="108" height="108" viewBox="0 0 108 108" fill="none" stroke="var(--yellow)" stroke-width="2"><circle cx="54" cy="54" r="52"/><circle cx="54" cy="54" r="18"/><path d="M54 22v8M54 78v8M22 54h8M78 54h8M31 31l6 6M71 71l6 6M31 77l6-6M71 37l6-6"/><circle cx="54" cy="54" r="26"/><path d="M46 54l6 6 10-12"/></svg>
<div class="benefit" style="left:101px;top:2562px">48 hour turn around guarantee – done in 48 hours or its free*</div>
<div class="vrule" style="left:292px"></div>

<svg class="abs" style="left:343px;top:2441px" width="108" height="108" viewBox="0 0 108 108" fill="none" stroke="var(--yellow)" stroke-width="2"><circle cx="54" cy="54" r="52"/><path d="M34 28h30l8 8v38H34zM40 42h26M40 50h26M40 58h18M28 34v46h30"/><circle cx="70" cy="72" r="9"/><path d="M64 78l12-12"/></svg>
<div class="benefit" style="left:312px;top:2562px">No pallet or outbound fees</div>
<div class="vrule" style="left:510px"></div>

<svg class="abs" style="left:555px;top:2445px" width="108" height="108" viewBox="0 0 108 108" fill="none" stroke="var(--yellow)" stroke-width="2"><circle cx="54" cy="54" r="52"/><rect x="30" y="22" width="48" height="14" rx="2"/><path d="M36 29h36"/><path d="M26 72h14l12 6h16l10-8M26 62h12l10 4h12"/><circle cx="66" cy="52" r="10"/><path d="M66 46v12"/></svg>
<div class="benefit" style="left:524px;top:2570px">No monthly subscription – only pay for what you use</div>
<div class="vrule" style="left:728px"></div>

<svg class="abs" style="left:767px;top:2445px" width="108" height="108" viewBox="0 0 108 108" fill="none" stroke="var(--yellow)" stroke-width="2"><circle cx="54" cy="54" r="52"/><rect x="44" y="24" width="20" height="18"/><rect x="32" y="44" width="20" height="18"/><rect x="56" y="44" width="20" height="18"/><path d="M24 66h60v8H24zM28 74v8M80 74v8M54 66v16"/></svg>
<div class="benefit" style="left:736px;top:2570px">No receiving fees</div>
<div class="vrule" style="left:946px"></div>

<svg class="abs" style="left:978px;top:2445px" width="108" height="108" viewBox="0 0 108 108" fill="none" stroke="var(--yellow)" stroke-width="2"><circle cx="54" cy="54" r="52"/><circle cx="50" cy="50" r="12"/><path d="M34 50a16 16 0 0 1 32 0M32 48v8h4v-8zM64 48v8h4v-8zM66 56c0 8-6 10-12 10M30 80c4-10 36-10 40 0"/><rect x="62" y="24" width="22" height="14" rx="3"/></svg>
<div class="benefit" style="left:947px;top:2570px">Email and phone support</div>

<!-- SOFTWARE -->
<section class="software">
  <svg class="abs" style="left:100px;top:106px" width="512" height="276" viewBox="0 0 512 276">
    <defs><linearGradient id="laptopTone" x1="0" y1="0" x2="1" y2="1"><stop offset="0" stop-color="#3a3f47"/><stop offset="1" stop-color="#1b1e23"/></linearGradient></defs>
    <g role="img" aria-label="Laptop showing the inventory tracking dashboard">
      <rect x="66" y="0" width="386" height="258" rx="10" fill="url(#laptopTone)"/>
      <rect x="78" y="12" width="362" height="234" fill="#e9ecef"/>
      <rect x="0" y="258" width="512" height="14" rx="6" fill="#c9ccd0"/>
    </g>
  </svg>
  <div class="sw-text">
    <h2 class="head">Our <span class="accent">software</span></h2>
    <p>Know what inventory is at our warehouse in real time. Our software allows you to track your inventory and know how your shipment status in real time. Professional software designed specifically for our needs.</p>
  </div>
</section>

<!-- CONTACT -->
<section class="contact">
  <div class="contact-yellow"></div>
  <div class="contact-photo" role="img" aria-label="Semi truck parked at sunset"></div>
  <h2 class="head">Get in touch</h2>
  <div class="sub">We're here to help <i></i></div>
  <div class="field" style="left:100px;top:189px;width:230px;height:38px">First Name:</div>
  <div class="field" style="left:343px;top:189px;width:230px;height:38px">Last Name:</div>
  <div class="field" style="left:100px;top:245px;width:230px;height:38px">Email:</div>
  <div class="field" style="left:343px;top:245px;width:230px;height:38px">Phone:</div>
  <div class="field" style="left:100px;top:300px;width:473px;height:76px">Message:</div>
  <span class="btn btn-line" style="left:100px;top:391px;width:152px;height:38px;font-size:13px">Submit Now</span>
</section>

<!-- FOOTER -->
<footer class="footer">
  <div class="logo" style="left:100px;top:140px;font-size:24px"><span class="dot"></span>HALVORN 3PL</div>

  <h4 style="left:368px;top:78px">Quick Link</h4>
  <ul style="left:368px;top:110px"><li>Home</li><li>About Us</li><li>Services</li><li>Software</li><li>Contact</li></ul>

  <h4 style="left:528px;top:78px">Contact Us</h4>
  <div class="c-item" style="left:528px;top:112px;width:230px"><svg width="14" height="18" viewBox="0 0 14 18"><path d="M7 0a7 7 0 0 0-7 7c0 5 7 11 7 11s7-6 7-11a7 7 0 0 0-7-7zm0 10a3 3 0 1 1 0-6 3 3 0 0 1 0 6z" fill="#fff"/></svg>4821 Harbor Lane Fairhaven USA<br>30418</div>
  <div class="c-item" style="left:528px;top:167px"><svg width="16" height="12" viewBox="0 0 16 12"><rect x=".5" y=".5" width="15" height="11" fill="none" stroke="#fff"/><path d="M1 1l7 6 7-6" fill="none" stroke="#fff"/></svg>Email:<br>info@halvorn3pl.com</div>
  <div class="c-item" style="left:528px;top:220px"><svg width="16" height="16" viewBox="0 0 24 24"><path d="M6.6 10.8a15 15 0 0 0 6.6 6.6l2.2-2.2c.3-.3.7-.4 1-.2 1.1.4 2.3.6 3.6.6.6 0 1 .4 1 1V20c0 .6-.4 1-1 1A17 17 0 0 1 3 4c0-.6.4-1 1-1h3.5c.6 0 1 .4 1 1 0 1.3.2 2.5.6 3.6.1.3 0 .7-.2 1z" fill="#fff"/></svg>Phone:<br>(123) 555 0198</div>

  <h4 style="left:812px;top:78px">Our Newsletter</h4>
  <div class="abs" style="left:812px;top:108px;font:400 13px var(--body)">Sign up to stay in the Halvorn Team</div>
  <div class="news-input">Enter Email
    <span class="send"><svg width="20" height="20" viewBox="0 0 24 24"><path d="M2 12l20-9-7 19-3-8z" fill="#141414"/></svg></span>
  </div>
  <span class="social" style="left:818px"></span>
  <span class="social" style="left:863px"></span>
  <span class="social" style="left:907px"></span>
  <span class="social" style="left:951px"></span>

  <div class="abs" style="left:93px;top:308px;width:1014px;height:1px;background:#444"></div>
  <div class="copyright">Copyright © 2021 halvorn 3pl . All rights</div>
</footer>

</body>
</html>
```